Tilwa Sandrim Construction
Business Cards, Note Pads, Envelopes, Letterhead , signboard etc.
Bright & Fun-filled
Hamdan R. Al-Qutami
CEO
P.O Box 40573
Al-Hassa 36417
Saudi Arabia
Hamdan@tilwasandrim.com.sa
www.tilwasandrim.com.sa
Leave the back of the business card to write all the information in arabic
similar logo

```html
<!DOCTYPE html>
<html lang="en">
<head>
<meta charset="utf-8">
<title>Tilwa Sandrim Construction – Business Card</title>
<link rel="stylesheet" href="https://fonts.googleapis.com/css2?family=Arimo:wght@400;700&display=swap">
<style>
  :root {
    --backdrop: #e9e7e4;
    --card: #ffffff;
    --brand-red: #b5121b;
    --swoosh-grey: #a7a9ac;
    --ink: #3b3b3b;
    --on-red: #ffffff;
  }
  html, body {
    margin: 0;
    width: 1200px;
    height: 769px;
    overflow: hidden;
    background: var(--backdrop);
    font-family: "Arimo", Arial, sans-serif;
  }
  .canvas {
    position: relative;
    width: 1200px;
    height: 769px;
  }
  .business-card {
    position: absolute;
    left: 210px;
    top: 140px;
    width: 780px;
    height: 490px;
    background: var(--card);
    border-radius: 26px;
    overflow: hidden;
    box-shadow: 0 2px 10px rgba(0,0,0,0.12);
  }
  .card-bands {
    position: absolute;
    inset: 0;
  }
  .holder {
    position: absolute;
    left: 56px;
    top: 26px;
    color: var(--on-red);
  }
  .holder-name {
    margin: 0;
    font-size: 21px;
    font-weight: 700;
  }
  .holder-title {
    margin: 4px 0 0;
    font-size: 19px;
    font-weight: 400;
  }
  .brand {
    position: absolute;
    left: 290px;
    top: 160px;
    width: 340px;
    display: flex;
    align-items: center;
    gap: 14px;
  }
  .brand-dot {
    width: 34px;
    height: 34px;
    border-radius: 50%;
    background: var(--brand-red);
    flex: none;
  }
  .brand-name {
    margin: 0;
    color: var(--brand-red);
    font-size: 30px;
    font-weight: 700;
    line-height: 1.1;
    letter-spacing: 0.5px;
  }
  .contact {
    position: absolute;
    left: 56px;
    top: 322px;
    margin: 0;
    color: var(--ink);
    font-size: 15px;
    line-height: 1.5;
    font-style: normal;
  }
  .contact span { display: block; }
</style>
</head>
<body>
<main class="canvas">
  <section class="business-card">
    <svg class="card-bands" viewBox="0 0 780 490" width="780" height="490" aria-hidden="true">
      <path d="M0 0 H780 V36 Q520 150 0 128 Z" fill="var(--brand-red)"/>
      <path d="M330 150 Q600 120 780 34" fill="none" stroke="var(--swoosh-grey)" stroke-width="9" stroke-linecap="round"/>
    </svg>

    <header class="holder">
      <h1 class="holder-name">Hamdan R. Al-Qutami</h1>
      <p class="holder-title">CEO</p>
    </header>

    <div class="brand">
      <span class="brand-dot"></span>
      <p class="brand-name">TILWA SANDRIM<br>CONSTRUCTION</p>
    </div>

    <address class="contact">
      <span>P.O Box 40573,  Al-Haasa 36417, Saudi Arabia</span>
      <span>P : +96635550142  |  C : +966505550187  |  F : +96635550199</span>
      <span>E : Hamdan@tilwasandrim.com.sa</span>
      <span>W : www.tilwasandrim.com.sa</span>
    </address>
  </section>
</main>
</body>
</html>
```